Lantern 58 Studios needs a web design

We need a website design for a California based visual effects (VFX) company to show potential clients and employees who we are and what we do. We are currently focusing on compositing based tasks such as but not limited to multi-pass composites, green screen extraction, rotoscope, paint fixes and retimes. We like imagery that makes people think of 'California' such as the state flag, sunshine and the beach. The website should send a message that although we are a new company, we are not new to the vfx industry. The website needs to be compatible with mobile devices. We also need the ability to edit and modify the site.

Target Market(s)

Studio executive, producers and potential employees.

Number of Pages Required

4 page

Font styles to use
Serif
Sans Serif

Requirements
Must have
• Must have space for company and individual biographies. Must have a page for a credits list and show reel. Must also have space for contact info ex. maps, email, social media.

```html
<!DOCTYPE html>
<html lang="en">
<head>
<meta charset="utf-8">
<title>Lantern 58 Studios</title>
<link href="https://fonts.googleapis.com/css2?family=Mulish:wght@400;600;700;800&display=swap" rel="stylesheet">
<style>
:root{
  --red:#a8282d;
  --red-deep:#8a1c21;
  --red-title:#b32a2f;
  --pink:#e6b3b3;
  --pink-soft:#f2d6d4;
  --ink:#333;
  --ink-soft:#555;
  --footer:#474747;
  --white:#fff;
}
*{margin:0;padding:0;box-sizing:border-box}
html,body{width:672px;height:1200px;overflow:hidden;background:var(--white)}
body{position:relative;font-family:"Mulish",sans-serif;color:var(--ink)}
.abs{position:absolute}

/* header */
.site-header{left:0;top:0;width:672px;height:52px;background:var(--white)}
.brand{left:12px;top:30px;display:flex;align-items:center;gap:5px;font-size:10px;font-weight:800;color:#222;letter-spacing:.2px}
.brand-dot{width:8px;height:8px;border-radius:50%;background:var(--red)}
.social{right:18px;top:7px;display:flex;gap:6px}
.social span{width:17px;height:17px;border-radius:50%;background:#555}
.main-nav{right:10px;top:37px;display:flex;gap:14px;font-size:5.6px;font-weight:600;color:#666;text-transform:uppercase}
.main-nav .current{color:var(--red)}
.header-rule{left:0;top:51px;width:672px;height:4px;background:var(--red-deep)}

/* hero */
.hero{left:0;top:55px;width:672px;height:194px;
  clip-path:polygon(0 0,100% 0,100% 160px,0 192px);
  background:linear-gradient(115deg,var(--red-deep) 0%,var(--red) 18%,#c9666a 35%,var(--pink-soft) 48%,#d48b8c 62%,var(--red) 80%,var(--red-deep) 100%)}
.hero-title{left:0;top:66px;width:672px;text-align:center;color:var(--white);font-size:18.5px;font-weight:800;line-height:23px}

/* production + news */
.section-title{font-size:13.5px;font-weight:800;color:#222}
.production-title{left:27px;top:280px}
.news-title{left:436px;top:270px}
.thumb{width:130px;height:73px;background:linear-gradient(180deg,#5d7fa8 0%,#9fb5cc 55%,#7a7f86 100%)}
.item-title{font-size:9.5px;font-weight:800;color:var(--red-title);margin-bottom:6px}
.item-text{font-size:8.3px;line-height:11.5px;color:var(--ink-soft)}
.production-item{left:27px;width:380px;display:flex;gap:16px}
.production-item .copy{width:230px;padding-top:0}
.news-item{left:436px;width:202px}
.news-rule{left:436px;width:200px;border-top:1.3px dashed #777}

/* about band */
.about{left:0;top:511px;width:672px;height:220px;background:var(--red)}
.about-art{right:0;top:0;width:300px;height:220px;
  background:linear-gradient(225deg,var(--pink) 0%,#c45a5e 30%,rgba(168,40,45,0) 70%)}
.about-art-low{left:360px;top:150px;width:180px;height:70px;
  background:linear-gradient(20deg,var(--red-deep) 0%,rgba(168,40,45,0) 80%)}
.about-body{left:0;top:22px;width:672px;text-align:center;color:var(--white)}
.about-body h2{font-size:12.5px;font-weight:800;margin-bottom:13px}
.about-body p{font-size:8.3px;line-height:11px;margin-bottom:10px}
.about-button{left:296px;top:682px;width:80px;height:20px;border-radius:10px;background:var(--white);color:var(--red);font-size:10.5px;font-weight:800;text-align:center;line-height:20px;letter-spacing:.6px}

/* team */
.portrait{width:122px;height:122px;border-radius:50%;border:2px solid var(--red);
  background:radial-gradient(circle at 50% 45%,#b08a76 0%,#7a6258 40%,#cfcfcf 75%)}
.bio-name{font-size:13px;font-weight:800;color:var(--red-title);letter-spacing:.3px}
.bio-text p{font-size:8.2px;line-height:11.3px;color:var(--ink-soft);margin-bottom:11px}

/* footer */
.site-footer{left:0;top:1160px;width:672px;height:40px;background:var(--footer);color:var(--white)}
.footer-note{left:27px;top:17px;font-size:5.4px}
.footer-nav{right:14px;top:17px;display:flex;gap:16px;font-size:5.4px;text-transform:uppercase}
</style>
</head>
<body>

<header class="site-header abs">
  <div class="brand abs"><span class="brand-dot"></span>LANTERN 58 STUDIOS</div>
  <div class="social abs"><span></span><span></span><span></span></div>
  <nav class="main-nav abs">
    <span class="current">Home</span><span>Creative</span><span>Studio</span><span>Motion Control</span><span>Pre-Viz Work</span><span>Gallery</span><span>Showreels</span><span>Contact</span>
  </nav>
</header>
<div class="header-rule abs"></div>

<section class="hero abs" role="img" aria-label="Low-poly pattern of red and pink triangles"></section>
<h1 class="hero-title abs">Meet the pioneers of live action motion control filming<br>and the rest of the creative department.</h1>

<h2 class="section-title production-title abs">Currently in Production</h2>
<article class="production-item abs" style="top:311px">
  <div class="thumb" role="img" aria-label="Photo of a cloudy blue sky over a skyline"></div>
  <div class="copy">
    <h3 class="item-title">Lorem ipsum dolor sit amet</h3>
    <p class="item-text">Lorem ipsum dolor sit amet, consectetur adipiscing elit. Ut pretium, risus finibus volutpat lobortis, sapien enim pellentesque tortor, sit amet molestie velit magna suscipit nibh.</p>
  </div>
</article>
<article class="production-item abs" style="top:411px">
  <div class="thumb" role="img" aria-label="Photo of a modern office building against the sky"></div>
  <div class="copy">
    <h3 class="item-title">Lorem ipsum dolor sit amet</h3>
    <p class="item-text">Lorem ipsum dolor sit amet, consectetur adipiscing elit. Ut pretium, risus finibus volutpat lobortis, sapien enim pellentesque tortor, sit amet molestie velit magna suscipit nibh.</p>
  </div>
</article>

<h2 class="section-title news-title abs">News</h2>
<article class="news-item abs" style="top:311px">
  <h3 class="item-title">Lorem ipsum dolor sit amet</h3>
  <p class="item-text">Lorem ipsum dolor sit amet, consectetur adipiscing elit. Ut pretium, risus finibus volutpat lobortis.</p>
</article>
<div class="news-rule abs" style="top:360px"></div>
<article class="news-item abs" style="top:372px">
  <h3 class="item-title">Lorem ipsum dolor sit amet</h3>
  <p class="item-text">Lorem ipsum dolor sit amet, consectetur adipiscing elit. Ut pretium, risus finibus volutpat lobortis.</p>
</article>
<div class="news-rule abs" style="top:421px"></div>
<article class="news-item abs" style="top:432px">
  <h3 class="item-title">Lorem ipsum dolor sit amet</h3>
  <p class="item-text">Lorem ipsum dolor sit amet, consectetur adipiscing elit. Ut pretium, risus finibus volutpat lobortis.</p>
</article>

<section class="about abs">
  <div class="about-art abs" role="img" aria-label="Low-poly pattern of red and pink triangles"></div>
  <div class="about-art-low abs" role="img" aria-label="Dark red triangle pattern"></div>
  <div class="about-body abs">
    <h2>Lantern 58</h2>
    <p>Formed in 2014, Lantern 58 Studios is a visual effects studio based in Costa Serena, CA.</p>
    <p>Taking their name from early Californian history, Lantern 58 Studios looks to continue the Golden State's tradition of strong and reliable visual effects.</p>
    <p>With close to 20 years in the vfx community, Lantern 58 Studios has the ability to service feature films, television,and commercials.<br>Lantern 58's capabilities are focused on compositing, 2.5D effects and environments, rotoscope, paint fixes, color timing and other 2D tasks.</p>
    <p>With a network of talented acquaintances built over the years, Lantern 58 Studios can adapt to the clients needs.<br>At a time when budgets and schedules are shrinking Lantern 58 Studios' goal is supplying world class visual effects work on a workable budget.</p>
  </div>
</section>
<div class="about-button abs">ABOUT US</div>

<div class="portrait abs" style="left:26px;top:770px" role="img" aria-label="Portrait photo of Owen Patrick Delaney"></div>
<h2 class="bio-name abs" style="left:215px;top:772px">Owen Patrick Delaney</h2>
<div class="bio-text abs" style="left:215px;top:802px;width:445px">
  <p>Owen Patrick Delaney grew up in Los Angeles and by the young age of 17 was working in the film industry as an on-set Production Assistant on 'The Courier'.</p>
  <p>By 1999, he began his long journey in to visual effects as a visual effects coordinator at Brightline<br>and Hale. As the Senior Manager of International Digital Production, Owen went on to develop several artist management teams as Brightline and Hale expanded globally.</p>
  <p>He acted as the main connection between Los Angeles and offices in Vancouver, Mumbai, Hyderabad, Malaysia and Taiwan focusing on artist growth and maintaining world class facilities. With on-set, visual effects and with international start ups knowledge, Owen has a range of experience that is difficult to find.</p>
</div>

<h2 class="bio-name abs" style="left:27px;top:970px">Danny Marlow</h2>
<div class="bio-text abs" style="left:27px;top:996px;width:420px">
  <p>Danny Marlow grew up in San Jose, CA reading comic books and Midnight Reels.</p>
  <p>Art and movies have always been a part of daily life. In 1997 Danny was given a chance to begin working in the visual effects industry as a generalist. He quickly gravitated to compositing and over his 17 year career, Danny has been fortunate enough to supervise and learn from various disciplines.</p>
  <p>With his compositing background always in mind, Danny has a unique perspective when it comes to creating visual effects.</p>
</div>
<div class="portrait abs" style="left:491px;top:970px" role="img" aria-label="Portrait photo of Danny Marlow"></div>

<footer class="site-footer abs">
  <div class="footer-note abs">Lantern 58 Studios © 2015 &nbsp;|&nbsp; All Rights Reserved</div>
  <nav class="footer-nav abs">
    <span>Home</span><span>Creative</span><span>Studio</span><span>Motion Control</span><span>Pre-Viz Work</span><span>Gallery</span><span>Showreels</span><span>Contact</span>
  </nav>
</footer>

</body>
</html>
```